Storm Restoration Contractor needs a professional business card design

Looking for a professional business card design. Not looking for your cheapo MS Word standard ones that are readily available. Dont want it to be cookie cutter look like ones readily available online. We just recently changed our logo and want to freshen up all our documents. Our company handles restoring a property back to a pre-loss condition after a storm damages it. For example, wind, hail, flood, fire losses.

Target Market(s)

Property Owners, Homeowners, Property Owners, Commercial Property Owners, Property Management Companies, Hail and Wind Damaged Properties

Industry/Entity Type

Construction Company

Contact Information for Business Card

Bramwell Outworks
555-418-7302
555-418-9047 fax
www.bramwelloutworks.example
info@bramwelloutworks.example

Requirements
Must have
• Clean, Professional, fresh look
• Storm Restoration, Roofing, Siding, Windows
Nice to have
• If there is a way to incorporate storms that may be cool.

```html
<!DOCTYPE html>
<html lang="en">
<head>
<meta charset="UTF-8">
<title>Bramwell Outworks – Business Card</title>
<link href="https://fonts.googleapis.com/css2?family=Exo+2:wght@600;700&family=Roboto:wght@400&display=swap" rel="stylesheet">
<style>
  :root {
    --backdrop: #b3b1b2;
    --brand-blue: #1a7fc4;
    --band-grey: #474a4d;
    --paper: #f6f6f6;
    --ink: #3a3d40;
    --ink-soft: #4b4e52;
    --white: #ffffff;
  }
  * { margin: 0; padding: 0; box-sizing: border-box; }
  html, body { width: 1200px; height: 1200px; overflow: hidden; }
  body { background: var(--backdrop); position: relative; font-family: "Roboto", sans-serif; }

  .card { position: absolute; width: 713px; height: 420px; overflow: hidden; }

  /* Front */
  .card-front { left: 238px; top: 117px; background: var(--brand-blue); }
  .front-mark {
    position: absolute; left: 268px; top: 44px; width: 178px; height: 178px;
    border: 9px solid var(--white); border-radius: 50%;
  }
  .front-name {
    position: absolute; left: 0; right: 0; top: 228px; text-align: center;
    font-family: "Exo 2", sans-serif; font-weight: 700; font-size: 29px;
    letter-spacing: 2px; text-transform: uppercase; color: var(--white);
  }
  .service-band {
    position: absolute; left: 0; right: 0; top: 308px; height: 41px;
    background: var(--band-grey); color: var(--white);
    font-family: "Exo 2", sans-serif; font-weight: 700; font-size: 21px;
    letter-spacing: 0.5px; text-transform: uppercase;
    display: flex; align-items: center; justify-content: center;
  }
  .web-line {
    position: absolute; left: 0; right: 0; top: 370px;
    display: flex; align-items: center; justify-content: center; gap: 18px;
    color: var(--white); font-size: 18px; letter-spacing: 1.4px;
  }
  .web-line svg { display: block; }

  /* Back */
  .card-back { left: 230px; top: 644px; background: var(--paper); }
  .back-brand { position: absolute; left: 45px; top: 53px; display: flex; align-items: center; gap: 18px; }
  .back-mark { width: 80px; height: 80px; border: 7px solid var(--brand-blue); border-radius: 50%; }
  .back-name {
    font-family: "Exo 2", sans-serif; font-weight: 700; font-size: 31px; line-height: 1.05;
    letter-spacing: 1px; text-transform: uppercase; color: var(--brand-blue);
  }
  .accent-right { position: absolute; right: 0; top: 44px; width: 16px; height: 95px; background: var(--brand-blue); }
  .accent-left { position: absolute; left: 0; top: 256px; width: 17px; height: 68px; background: var(--band-grey); }
  .person { position: absolute; left: 45px; top: 259px; }
  .person-name {
    font-family: "Exo 2", sans-serif; font-weight: 700; font-size: 28px;
    letter-spacing: 2px; text-transform: uppercase; color: var(--brand-blue);
  }
  .person-title { font-size: 17px; color: var(--ink-soft); margin-top: 2px; }
  .contact-list { position: absolute; left: 380px; top: 259px; list-style: none; }
  .contact-list li {
    display: flex; align-items: center; gap: 19px; height: 27.7px;
    font-size: 18px; color: var(--ink);
  }
  .contact-list svg { width: 18px; height: 16px; fill: var(--brand-blue); flex: none; }
  .contact-list .accent { color: var(--brand-blue); }
</style>
</head>
<body>

<section class="card card-front">
  <div class="front-mark"></div>
  <h1 class="front-name">Bramwell Outworks</h1>
  <div class="service-band">Storm Restoration&nbsp;&nbsp;|&nbsp;&nbsp;Roofing&nbsp;&nbsp;|&nbsp;&nbsp;Siding&nbsp;&nbsp;|&nbsp;&nbsp;Windows</div>
  <div class="web-line">
    <svg width="75" height="6" viewBox="0 0 75 6"><polygon points="0,3 75,0 75,6" fill="#fff"/></svg>
    <span>www.bramwelloutworks.example</span>
    <svg width="75" height="6" viewBox="0 0 75 6"><polygon points="0,0 75,3 0,6" fill="#fff"/></svg>
  </div>
</section>

<section class="card card-back">
  <div class="back-brand">
    <div class="back-mark"></div>
    <div class="back-name">Bramwell<br>Outworks</div>
  </div>
  <div class="accent-right"></div>
  <div class="accent-left"></div>

  <div class="person">
    <div class="person-name">Dana Whitlock</div>
    <div class="person-title">Managing Director</div>
  </div>

  <ul class="contact-list">
    <li>
      <svg viewBox="0 0 18 16"><path d="M1 5c0-3 4-4 8-4s8 1 8 4l-3 1-1-2H5L4 6zM4 8h10l2 7H2z"/></svg>
      555-418-7302
    </li>
    <li>
      <svg viewBox="0 0 18 16"><path d="M5 0h8v5H5zM1 6h16v7h-3v3H4v-3H1zM6 11v3h6v-3z"/></svg>
      555-418-9047 fax
    </li>
    <li>
      <svg viewBox="0 0 18 16"><path d="M1 2h16v12H1zM3 4l6 5 6-5v2l-6 5-6-5z" fill-rule="evenodd"/></svg>
      info@bramwelloutworks.example
    </li>
    <li>
      <svg viewBox="0 0 18 16"><circle cx="9" cy="8" r="7" fill="none" stroke="#1a7fc4" stroke-width="1.5"/><path d="M2 8h14M9 1v14" stroke="#1a7fc4" stroke-width="1.2"/><ellipse cx="9" cy="8" rx="3" ry="7" fill="none" stroke="#1a7fc4" stroke-width="1.2"/></svg>
      <span>www.<span class="accent">bramwelloutworks</span>.example</span>
    </li>
  </ul>
</section>

</body>
</html>
```